Flyer für freiberuflichen Bauingenieur
Zielgruppe
Ich bin freiberuflicher Bauingenieur und erstelle vermehrt Schadstoffkataster für zum Abbruch vorgesehene Gebäude im Auftrag von Abbruchunternehmen und Eigentümern.
Aufgabenstellung
Ich habe die Rahmenbedingungen in eine Worddatei geschrieben, auch vorgesehenes Format Farben etc.

```html
<!DOCTYPE html>
<html lang="de">
<head>
<meta charset="utf-8">
<title>Flyer Bauplanungs- und Ingenieurbüro</title>
<link rel="stylesheet" href="https://fonts.googleapis.com/css2?family=Cabin:wght@400;600;700&family=Open+Sans:wght@400;800&family=Kalam:wght@400&display=swap">
<style>
  :root{
    --bg:#e6e6e6;
    --paper:#ffffff;
    --blue:#0d5a80;
    --green:#6b9a12;
    --pale:#d6dcae;
    --grey:#7d7d7d;
    --ink:#1c1c1c;
  }
  html,body{margin:0;padding:0;overflow:hidden;}
  body{width:1200px;height:1200px;background:var(--bg);}
  .flyer{position:absolute;left:0;top:0;width:1200px;height:1200px;}
  .script{font-family:'Kalam',cursive;fill:var(--blue);}
  .contact{font-family:'Cabin',sans-serif;}
  .contact .name{fill:var(--blue);font-weight:600;font-size:15px;}
  .contact .office{fill:var(--ink);font-weight:600;font-size:15px;}
  .contact .line{fill:var(--grey);font-size:14px;}
  .label{font-family:'Open Sans',sans-serif;font-size:12.5px;letter-spacing:.5px;fill:var(--ink);}
  .hub-name{font-family:'Cabin',sans-serif;font-weight:600;font-size:13px;fill:var(--green);}
  .headline{font-family:'Open Sans',sans-serif;font-weight:800;font-size:36px;fill:var(--blue);}
  .subline{font-family:'Open Sans',sans-serif;font-weight:400;font-size:30px;fill:var(--blue);}
</style>
</head>
<body>
<svg class="flyer" viewBox="0 0 1200 1200" xmlns="http://www.w3.org/2000/svg">
  <defs>
    <linearGradient id="demolition" x1="0" y1="0" x2="0" y2="1">
      <stop offset="0" stop-color="#4a86d4"/><stop offset=".5" stop-color="#9a7a5c"/><stop offset="1" stop-color="#5f6a3c"/>
    </linearGradient>
    <linearGradient id="asbestos" x1="0" y1="0" x2="1" y2="1">
      <stop offset="0" stop-color="#6a7040"/><stop offset=".6" stop-color="#9a9a94"/><stop offset="1" stop-color="#5c6436"/>
    </linearGradient>
    <linearGradient id="insulation" x1="0" y1="0" x2="0" y2="1">
      <stop offset="0" stop-color="#e4c7a4"/><stop offset=".5" stop-color="#c8d2dc"/><stop offset="1" stop-color="#3f6a2a"/>
    </linearGradient>
    <linearGradient id="stairs" x1="0" y1="0" x2="1" y2="1">
      <stop offset="0" stop-color="#4b4f55"/><stop offset=".55" stop-color="#7a6258"/><stop offset="1" stop-color="#a85c4a"/>
    </linearGradient>
    <linearGradient id="panels" x1="0" y1="0" x2="0" y2="1">
      <stop offset="0" stop-color="#d8cca6"/><stop offset="1" stop-color="#c9bc94"/>
    </linearGradient>
    <linearGradient id="crane" x1="0" y1="0" x2="0" y2="1">
      <stop offset="0" stop-color="#f7f7f7"/><stop offset="1" stop-color="#f1f1f1"/>
    </linearGradient>
  </defs>

  <g class="page" transform="translate(185,20)">
    <rect width="830" height="1160" rx="14" fill="var(--paper)"/>

    <!-- heading -->
    <text class="script" x="60" y="100" font-size="36">Planung, Bauleitung</text>
    <text class="script" x="64" y="150" font-size="36">und mehr …</text>

    <!-- connectors -->
    <g stroke="var(--green)" stroke-width="1.5">
      <line x1="324" y1="472" x2="156" y2="303"/>
      <line x1="324" y1="472" x2="349" y2="280"/>
      <line x1="324" y1="472" x2="167" y2="510"/>
      <line x1="324" y1="472" x2="275" y2="713"/>
      <line x1="324" y1="472" x2="478" y2="541"/>
    </g>

    <!-- outline circles -->
    <g fill="none" stroke="var(--pale)" stroke-width="1.5">
      <circle cx="270" cy="202" r="56"/>
      <circle cx="456" cy="308" r="49"/>
      <circle cx="128" cy="634" r="76"/>
      <circle cx="199" cy="822" r="115"/>
      <circle cx="490" cy="652" r="88"/>
    </g>

    <!-- photo areas -->
    <g stroke="var(--blue)" stroke-width="4">
      <circle cx="156" cy="303" r="98" fill="url(#demolition)" role="img" aria-label="Foto: teilweise abgerissenes Fachwerkhaus"/>
      <circle cx="349" cy="280" r="71" fill="url(#asbestos)" role="img" aria-label="Foto: gebrochene Asbestzementplatte im Gras"/>
      <circle cx="167" cy="510" r="71" fill="url(#insulation)" role="img" aria-label="Foto: freigelegte Dämmung an einer Hauswand"/>
      <circle cx="275" cy="713" r="98" fill="url(#stairs)" role="img" aria-label="Foto: Kellertreppe aus Klinker mit beschichteter Wand"/>
      <circle cx="478" cy="541" r="61" fill="url(#panels)" role="img" aria-label="Foto: Fassadenplatten"/>
    </g>

    <!-- center hub: plain circle with name -->
    <circle cx="324" cy="472" r="46" fill="#fff" stroke="var(--green)" stroke-width="4"/>
    <text class="hub-name" x="324" y="477" text-anchor="middle">Hellberg</text>

    <!-- labels -->
    <text class="label" transform="translate(236,222) rotate(-45)">ABBRÜCHE</text>
    <text class="label" transform="translate(430,318) rotate(14)">TRGS 519</text>
    <text class="label" transform="translate(426,336) rotate(14)">ASBEST</text>
    <g class="label" transform="translate(78,668) rotate(-68)">
      <text x="0" y="0">SCHADSTOFF-</text>
      <text x="10" y="18">UNTER-</text>
      <text x="-8" y="36">SUCHUNGEN</text>
    </g>
    <g class="label" transform="translate(120,865) rotate(-53)">
      <text x="0" y="0">NACHWEIS DER</text>
      <text x="0" y="18">BELASTUNG/</text>
      <text x="-4" y="36">BELASTUNGS-</text>
      <text x="36" y="54">FREIHEIT</text>
    </g>
    <g class="label" transform="translate(482,708) rotate(-90)">
      <text x="0" y="0">GEFAHRSTOFF-</text>
      <text x="4" y="18">VERORDNUNG</text>
    </g>

    <!-- crane -->
    <rect x="452" y="740" width="364" height="218" fill="url(#crane)" role="img" aria-label="Illustration: Baukran in weißen Linien"/>

    <!-- contacts -->
    <g class="contact" text-anchor="end">
      <text class="name" x="760" y="66">Jonas Hellberg Dipl.-Ing. (FH)</text>

      <text class="office" x="760" y="108">Ebersrode (Hauptsitz)</text>
      <text class="line" x="760" y="148">Lindenallee 7</text>
      <text class="line" x="760" y="168">29111 Ebersrode</text>
      <text class="line" x="760" y="210">+49 (0) 55 12 / 3 48 17</text>
      <text class="line" x="760" y="230">+49 (0) 170 /42 61 73 90</text>
      <text class="line" x="760" y="250">info(at)hellberg-bau.de</text>

      <text class="office" x="760" y="290">Büro Kranzfeld</text>
      <text class="line" x="760" y="330">Mühlenweg 18</text>
      <text class="line" x="760" y="350">21999 Hasenbrook</text>
      <text class="line" x="760" y="392">+49 (0) 40 99 / 55 12 348</text>
      <text class="line" x="760" y="412">+49 (0) 170 /42 61 73 90</text>
      <text class="line" x="760" y="432">kranzfeld(at)hellberg-bau.de</text>

      <text class="office" x="760" y="482">Büro Osterwalde</text>
      <text class="office" x="760" y="516">Büro Birkmoor</text>
      <text class="line" x="760" y="556">Am Feldrain 4</text>
      <text class="line" x="760" y="576">23999 Birkmoor</text>
      <text class="line" x="760" y="616">(Festnetz folgt)</text>
      <text class="line" x="760" y="636">+49 (0) 170 /42 61 73 90</text>
      <text class="line" x="760" y="656">sh(at)hellberg-bau.de</text>
    </g>

    <!-- office icons -->
    <g fill="var(--green)">
      <circle cx="598" cy="103" r="11"/>
      <circle cx="640" cy="285" r="11"/>
      <circle cx="630" cy="477" r="11"/>
      <circle cx="652" cy="511" r="11"/>
    </g>
    <g fill="#fff">
      <path d="M592 106 L598 99 L604 106 L604 110 L592 110 Z"/>
      <path d="M634 288 L640 281 L646 288 L646 292 L634 292 Z"/>
      <path d="M624 480 L630 473 L636 480 L636 484 L624 484 Z"/>
      <path d="M646 514 L652 507 L658 514 L658 518 L646 518 Z"/>
    </g>

    <!-- phone / mail icons -->
    <g fill="var(--blue)">
      <circle cx="784" cy="214" r="11"/><circle cx="784" cy="244" r="11"/>
      <circle cx="784" cy="396" r="11"/><circle cx="784" cy="426" r="11"/>
      <circle cx="784" cy="626" r="11"/><circle cx="784" cy="652" r="11"/>
    </g>
    <g fill="none" stroke="#fff" stroke-width="1.4">
      <rect x="780" y="207" width="8" height="14" rx="1.5"/>
      <rect x="780" y="389" width="8" height="14" rx="1.5"/>
      <rect x="780" y="619" width="8" height="14" rx="1.5"/>
      <rect x="777" y="239" width="14" height="10"/><path d="M777 239 L784 245 L791 239"/>
      <rect x="777" y="421" width="14" height="10"/><path d="M777 421 L784 427 L791 421"/>
      <rect x="777" y="647" width="14" height="10"/><path d="M777 647 L784 653 L791 647"/>
    </g>

    <!-- footer -->
    <text class="headline" x="66" y="1000" textLength="712" lengthAdjust="spacingAndGlyphs">DIPL.-ING. JONAS HELLBERG</text>
    <line x1="66" y1="1016" x2="778" y2="1016" stroke="var(--green)" stroke-width="2"/>
    <text class="subline" x="66" y="1060" textLength="712" lengthAdjust="spacingAndGlyphs">BAUPLANUNGS- UND INGENIEURBÜRO</text>
    <rect x="56" y="1086" width="740" height="6" fill="#fff" stroke="#d4d4d4" stroke-width="1"/>
  </g>
</svg>
</body>
</html>
```